New education centre needs a flyer design

We need a flyer design for this coming holiday program in science for students in primary school. Its a science program for 2 days in which experiments, applications will be conducted to teach a concept. I will attach what we will be doing but the description needs to be as brief as possible so that viewers who see it will be interested and call to find out more. I leave the design and colors to you but it has to be attractive and eye catching. Please see attach for information on details of the program as well as the logo of our education centre in Singapore.
Primary School Students and Parents
Education

```html
<!DOCTYPE html>
<html lang="en">
<head>
<meta charset="utf-8">
<title>Sparkhill Campus – Holiday Science Camp Flyer</title>
<link rel="stylesheet" href="https://fonts.googleapis.com/css2?family=Comfortaa:wght@600&family=Comic+Neue:wght@400;700&family=Kalam:wght@400&family=Roboto:wght@400;700&display=swap">
<style>
  :root{
    --navy:#1b2152;
    --navy-deep:#12163d;
    --navy-glow:#2a3a78;
    --orange:#f6a723;
    --white:#ffffff;
    --band-grey:#c9ccd4;
    --photo-warm:#d9c3ae;
    --photo-light:#eef0f2;
  }
  *{margin:0;padding:0;box-sizing:border-box}
  html,body{width:874px;height:1200px;overflow:hidden;background:var(--navy-deep)}
  .flyer{
    position:relative;width:874px;height:1200px;overflow:hidden;
    background:radial-gradient(ellipse at 60% 45%, var(--navy-glow) 0%, var(--navy) 45%, var(--navy-deep) 100%);
    color:var(--white);
    font-family:"Comic Neue", "Comic Sans MS", cursive;
  }
  .brand{
    position:absolute;left:38px;top:32px;width:210px;height:210px;border-radius:50%;
    background:var(--white);display:flex;align-items:center;justify-content:center;text-align:center;
    color:var(--navy);font-family:"Comic Neue", cursive;font-weight:700;font-size:30px;line-height:1.1;
  }
  .headline{
    position:absolute;right:34px;top:34px;
    font-family:"Comfortaa", sans-serif;font-weight:600;font-size:36px;letter-spacing:.5px;
  }
  .teaser{
    position:absolute;right:28px;top:92px;text-align:right;
    font-size:21px;line-height:31px;font-weight:700;
  }
  .band{position:absolute;left:0;top:0;width:874px;height:1200px}
  .camp-note{
    position:absolute;right:28px;top:700px;text-align:right;color:var(--orange);
    font-family:"Kalam", cursive;font-size:27px;line-height:35px;
  }
  .camp-note .big{font-size:33px}
  .details{position:absolute;left:38px;right:38px;top:843px;font-size:24px;line-height:30px;text-align:justify}
  .details p + p{margin-top:20px}
  .call{position:absolute;left:40px;top:1063px;font-size:31px;font-weight:700;letter-spacing:.3px}
  .limited{position:absolute;left:40px;top:1110px;font-size:24px;font-weight:700}
  .footer{
    position:absolute;left:0;right:0;top:1152px;height:48px;border-top:3px solid var(--orange);
    display:flex;align-items:center;justify-content:space-between;padding:0 28px 0 30px;
    font-family:"Roboto", sans-serif;font-size:14px;
  }
  .footer-item{display:flex;align-items:center;gap:6px}
  .footer-phone{font-size:24px;font-weight:700;color:var(--white)}
  .footer svg{flex:none}
</style>
</head>
<body>
<div class="flyer">

  <svg class="band" viewBox="0 0 874 1200" aria-hidden="false">
    <defs>
      <linearGradient id="photoTone" x1="0" y1="0" x2="1" y2="1">
        <stop offset="0" stop-color="var(--photo-light)"/>
        <stop offset=".45" stop-color="var(--photo-warm)"/>
        <stop offset=".75" stop-color="#f1f2f4"/>
        <stop offset="1" stop-color="#b59a80"/>
      </linearGradient>
    </defs>
    <!-- grey frame behind the photo area -->
    <polygon points="0,386 318,214 874,214 874,656 576,656 490,770 0,770" fill="var(--band-grey)"/>
    <polygon role="img" aria-label="Photo: a smiling teacher and two pupils wiring a battery and bulb circuit on a wooden board"
      points="0,394 323,222 874,222 874,648 569,648 483,761 0,761" fill="url(#photoTone)"/>
    <!-- orange circuit lines -->
    <polyline points="36,364 154,364 327,192 874,192" fill="none" stroke="var(--orange)" stroke-width="5"/>
    <circle cx="36" cy="364" r="14" fill="var(--orange)"/>
    <polyline points="0,790 483,790 587,677 824,677" fill="none" stroke="var(--orange)" stroke-width="5"/>
    <circle cx="824" cy="677" r="14" fill="var(--orange)"/>
  </svg>

  <div class="brand">Sparkhill<br>Campus</div>

  <h1 class="headline">Home alone?</h1>
  <p class="teaser">Ever thought of making your very OWN burglar alarm<br>to feel safe and impress your family and friends?</p>

  <p class="camp-note">In our <span class="big">holiday camp,</span><br>this is exactly what<br>we are going to be doing!!</p>

  <div class="details">
    <p>We are going to guide you to build unique items by discovering what electricity is all about in a fun and exciting way by touching base on lights, batteries, electrical circuits and more.</p>
    <p>Don’t wait any longer! Be prepared to let your creative juices flow and your imagination come alive by creating your very own personalized electrical items!</p>
  </div>

  <p class="call">Call us at 62109385 to reserve your places now.</p>
  <p class="limited">Limited slots available.</p>

  <footer class="footer">
    <span class="footer-item">
      <svg width="12" height="17" viewBox="0 0 12 17"><path d="M6 0a6 6 0 0 1 6 6c0 4.5-6 11-6 11S0 10.5 0 6a6 6 0 0 1 6-6z" fill="var(--orange)"/><circle cx="6" cy="6" r="2.3" fill="var(--navy)"/></svg>
      118 Meadow Lane Road Singapore 408812
    </span>
    <span class="footer-item footer-phone">
      <svg width="24" height="24" viewBox="0 0 24 24"><circle cx="12" cy="12" r="10.5" fill="none" stroke="var(--orange)" stroke-width="2"/><path d="M9 6.5l2 2.6-1.3 1.5c.7 1.6 1.9 2.8 3.5 3.6l1.5-1.3 2.6 2-1.3 2.2c-4.3-.4-8.3-4.4-8.7-8.7z" fill="var(--orange)"/></svg>
      62109385
    </span>
    <span class="footer-item">
      <svg width="22" height="15" viewBox="0 0 22 15"><rect x="1" y="1" width="20" height="13" rx="1" fill="var(--orange)"/><polyline points="1,1 11,9 21,1" fill="none" stroke="var(--navy)" stroke-width="1.6"/></svg>
      hello@sparkhillcampus.sg
    </span>
  </footer>

</div>
</body>
</html>
```